Upgrades and adjustments to my existing website

I currently have a website in the trial period with HostBramble but their template isn't meeting my site needs. My website is https://www.QuorvaPosts.example. I need the calendar to be changed. Each customer that orders a real estate sign installation from us needs to be able to request a day (not time specific) and be able to enter the address of the home where they need the sign installed. In addition, I would like a testimonials section on the website. I need someone to build the website and point it to my domain name as I do not know how to do any of that. My customers are trying to order now so every day they can't place the order I am losing money so quick turn time is important

Target Market(s)

Real Estate Agents ordering sign post installations

Industry/Entity Type

Real Estate

Coding

Coded - Design and coding required

Number of Pages Required

1 page

Font styles to use
Sans Serif

Colors
0355a3
3377b5
85abd2
0493ce
33a6d7
85cae6

Requirements
Must have
• The ability to book installation requests online with address for installation. Please see live current website I have
Nice to have
• Links to social media, ability to pay invoice on website,
Testimonial section.
Ability to track progress of installation request for customers
Ability to share the appointment calendar with my installers

```html
<!DOCTYPE html>
<html lang="en">
<head>
<meta charset="utf-8">
<title>Quorva Posts – Lit Real Estate Sign Installation</title>
<link href="https://fonts.googleapis.com/css2?family=Bebas+Neue&family=Lato:ital,wght@0,400;0,700;0,900;1,700&family=Poppins:ital,wght@0,400;0,500;0,600;1,400&display=swap" rel="stylesheet">
<style>
:root{
  --navy:#173a5a;
  --navy-deep:#10304d;
  --blue:#0355a3;
  --blue-mid:#3377b5;
  --blue-soft:#85abd2;
  --sky:#0493ce;
  --sky-mid:#33a6d7;
  --sky-soft:#85cae6;
  --button:#2389e2;
  --nav-active:#3ca0e8;
  --ink:#1a1a1a;
  --text:#4a4a4a;
  --muted:#6a6a6a;
  --line:#d9d9d9;
  --day-bg:#eef6e4;
  --day-ink:#86ad3f;
  --white:#ffffff;
}
*{box-sizing:border-box;margin:0;padding:0}
html,body{width:1200px;height:3597px;overflow:hidden}
body{position:relative;background:var(--white);font-family:"Lato",sans-serif;color:var(--text)}
.abs{position:absolute}
.display{font-family:"Bebas Neue",sans-serif;color:var(--ink);letter-spacing:.5px;line-height:1}
.pill{position:absolute;display:flex;align-items:center;justify-content:center;background:var(--button);color:var(--white);border-radius:30px;font-family:"Lato",sans-serif;font-weight:700;font-size:16px}

/* header */
.site-header{position:absolute;left:0;top:0;width:1200px;height:105px;background:var(--navy)}
.brand{position:absolute;display:flex;align-items:center;gap:8px;color:var(--white);font-family:"Lato",sans-serif;font-weight:900;font-size:22px}
.brand-square{width:14px;height:14px;background:var(--sky-mid)}
.header-phone{left:600px;top:15px;color:var(--white);font-size:20px;font-weight:700;display:flex;align-items:center;gap:8px}
.social{position:absolute;width:38px;height:38px;border:2px solid var(--white);border-radius:50%}
.main-nav{position:absolute;top:64px;left:0;width:1200px;height:24px}
.main-nav a{position:absolute;transform:translateX(-50%);color:var(--white);text-decoration:none;font-weight:700;font-size:16px;white-space:nowrap}
.main-nav a.active{color:var(--nav-active)}

/* hero */
.hero{position:absolute;left:0;top:105px;width:1200px;height:600px;background:linear-gradient(100deg,#1d1611 0%,#3a2a1c 35%,#2a2420 60%,#5c4a52 78%,#1b1714 100%)}
.hero-title{left:110px;top:292px;font-size:52px;color:var(--white)}
.hero-copy{left:110px;top:375px;width:420px;color:var(--white);font-size:17px;line-height:25px}
.hero-arrow{position:absolute;top:388px}
.dot{position:absolute;top:662px;width:14px;height:14px;border-radius:50%;background:#8a8a8a}
.dot.on{background:var(--white)}

/* about */
.about-frame{left:141px;top:789px;width:424px;height:394px;background:var(--navy)}
.about-photo{left:150px;top:797px;width:423px;height:395px;background:linear-gradient(180deg,#5fa6d8 0%,#9ab8c9 45%,#8c7a62 70%,#6d5a45 100%)}
.about-title{left:637px;top:790px;font-size:46px}
.about-sub{left:637px;top:845px;font-family:"Lato",sans-serif;font-style:italic;font-weight:700;font-size:25px;color:var(--blue)}
.about-copy{left:637px;top:888px;width:422px;font-size:14.5px;line-height:28.4px;text-align:justify;color:var(--text)}

/* booking */
.booking{position:absolute;left:0;top:1276px;width:1200px;height:590px;background:linear-gradient(135deg,#1b4266 0%,var(--navy-deep) 50%,#163a5a 100%)}
.calendar{position:absolute;left:113px;top:1368px;width:412px;height:413px;background:var(--white);font-family:"Poppins",sans-serif}
.cal-head{height:67px;background:var(--button);display:flex;align-items:center;justify-content:space-between;padding:0 40px;color:var(--white);font-size:25px;font-weight:500}
.cal-grid{display:grid;grid-template-columns:repeat(7,1fr)}
.cal-grid span{display:flex;align-items:center;justify-content:center;height:58px;border-right:1px solid var(--line);border-bottom:1px solid var(--line);font-size:20px;color:#333}
.cal-grid span:nth-child(7n){border-right:none}
.cal-grid .dow{height:56px;background:var(--day-bg);color:var(--day-ink);font-weight:500;border:none}
.booking-title{left:555px;top:1372px;font-size:39px;line-height:43px;color:var(--white)}
.event-card{position:absolute;left:559px;width:550px;height:116px;background:var(--white);border:2px solid #7aa4c7}
.event-label{position:absolute;left:18px;top:16px;font-weight:900;font-size:16px;color:var(--ink)}
.event-name{position:absolute;left:18px;top:42px;font-weight:700;font-size:21px;color:#333}
.event-meta{position:absolute;left:18px;top:78px;font-size:14px;color:#333;display:flex;align-items:center;gap:6px}
.event-photo{position:absolute;right:0;top:0;width:145px;height:112px}

/* testimonials */
.section-title{font-size:46px}
.avatar{position:absolute;width:67px;height:67px;border-radius:50%;background:linear-gradient(180deg,#d9c6b5,#b08f78)}
.quote{position:absolute;width:400px;font-family:"Poppins",sans-serif;font-style:italic;font-size:14px;line-height:28.5px;color:#555}
.quote-name{position:absolute;font-family:"Poppins",sans-serif;font-weight:600;font-size:19px;color:var(--ink)}
.quote-role{position:absolute;font-family:"Poppins",sans-serif;font-size:13px;color:var(--muted)}

/* map */
.map{position:absolute;left:0;top:2277px;width:1200px;height:395px;background:linear-gradient(160deg,#eeeeee,#e2e2e2)}

/* contact */
.contact-title{left:136px;top:2742px;font-size:42px}
.contact-lede{left:136px;top:2794px;font-size:17px;color:#333}
.info-label{position:absolute;left:180px;font-weight:700;font-size:20px;color:var(--ink)}
.info-text{position:absolute;left:182px;font-size:14px;line-height:20px;color:#444}
.field{position:absolute;border:1px solid #dcdcdc;background:var(--white);font-size:13px;color:#555;padding:16px 19px}

/* footer */
.site-footer{position:absolute;left:0;top:3216px;width:1200px;height:381px;background:var(--navy)}
.footer-nav a{position:absolute;top:3434px;transform:translateX(-50%);color:var(--white);font-weight:700;font-size:17px;text-decoration:none;white-space:nowrap}
.copyright{left:0;width:1200px;top:3553px;text-align:center;color:var(--white);font-size:15px}
</style>
</head>
<body>

<header class="site-header">
  <div class="brand" style="left:112px;top:38px"><span class="brand-square"></span>Quorva Posts</div>
  <div class="abs header-phone">
    <svg width="16" height="16" viewBox="0 0 24 24"><path d="M6.6 10.8a15.1 15.1 0 0 0 6.6 6.6l2.2-2.2c.3-.3.7-.4 1-.2 1.1.4 2.3.6 3.6.6.6 0 1 .4 1 1V20c0 .6-.4 1-1 1C10.6 21 3 13.4 3 4c0-.6.4-1 1-1h3.5c.6 0 1 .4 1 1 0 1.3.2 2.5.6 3.6.1.3 0 .7-.2 1z" fill="#fff"/></svg>
    Call Us Today: +1 555-014-2290
  </div>
  <span class="social" style="left:917px;top:11px"></span>
  <span class="social" style="left:961px;top:11px"></span>
  <span class="social" style="left:1006px;top:11px"></span>
  <span class="social" style="left:1049px;top:11px"></span>
  <nav class="main-nav">
    <a class="active" style="left:411px">HOME</a>
    <a style="left:533px">ABOUT US</a>
    <a style="left:667px">SERVICES</a>
    <a style="left:786px">EVENT</a>
    <a style="left:900px">REVIEW</a>
    <a style="left:1039px">CONTACT US</a>
  </nav>
</header>

<section class="hero" role="img" aria-label="Night-time photo of a lit for-sale sign post in front of a brick home"></section>
<h1 class="abs display hero-title">WELCOME TO QUORVA POSTS</h1>
<p class="abs hero-copy">Lorem ipsum dolor sit amet, consectetur adipiscing elit, sed do eiusmod tempor incididunt ut</p>
<a class="pill" style="left:110px;top:447px;width:155px;height:46px">GET STARTED</a>
<svg class="hero-arrow" style="left:62px" width="20" height="36" viewBox="0 0 20 36"><path d="M17 2 3 18l14 16" stroke="#fff" stroke-width="2.5" fill="none"/></svg>
<svg class="hero-arrow" style="left:1114px" width="20" height="36" viewBox="0 0 20 36"><path d="M3 2l14 16L3 34" stroke="#fff" stroke-width="2.5" fill="none"/></svg>
<span class="dot" style="left:557px"></span>
<span class="dot" style="left:581px"></span>
<span class="dot" style="left:604px"></span>
<span class="dot on" style="left:627px"></span>

<div class="abs about-frame"></div>
<div class="abs about-photo" role="img" aria-label="Photo of the owner leaning on a white sign post in a park"></div>
<h2 class="abs display about-title">ABOUT US</h2>
<p class="abs about-sub">Don’t sell your home in the dark</p>
<p class="abs about-copy">We install solar powered lit real estate signs to make your home stand out and get it sold. We use treated wood posts with powder-coated steel bases for high quality, looks and durability. Your order includes storage, maintenance, and installation of your panels and riders within 48 hours, as well as free pick-up and removal. We are fully insured. Our Owner and Operator, Marcus, is committed to providing an excellent product and exceptional service.</p>
<a class="pill" style="left:637px;top:1139px;width:155px;height:46px;font-weight:400">CONTACT US</a>

<section class="booking" role="img" aria-label="Dark blue faceted background"></section>
<div class="calendar">
  <div class="cal-head">
    <svg width="12" height="14" viewBox="0 0 12 14"><path d="M10 0v14L0 7z" fill="#fff"/></svg>
    FEBRUARY 2021
    <svg width="12" height="14" viewBox="0 0 12 14"><path d="M2 0v14l10-7z" fill="#fff"/></svg>
  </div>
  <div class="cal-grid">
    <span class="dow">Sun</span><span class="dow">Mon</span><span class="dow">Tue</span><span class="dow">Wed</span><span class="dow">Thu</span><span class="dow">Fri</span><span class="dow">Sat</span>
    <span></span><span>1</span><span>2</span><span>3</span><span>4</span><span>5</span><span>6</span>
    <span>7</span><span>8</span><span>9</span><span>10</span><span>11</span><span>12</span><span>13</span>
    <span>14</span><span>15</span><span>16</span><span>17</span><span>18</span><span>19</span><span>20</span>
    <span>21</span><span>22</span><span>23</span><span>24</span><span>25</span><span>26</span><span>27</span>
    <span>28</span><span></span><span></span><span></span><span></span><span></span><span></span>
  </div>
</div>
<h2 class="abs display booking-title">ONLINE APPOINTMENTS. SELECT ANY TIME<br>AND WE WILL INSTALL WITHIN 48 HOURS</h2>
<article class="event-card" style="top:1475px">
  <span class="event-label">EVENTS</span>
  <span class="event-name">Real Estate Sign Installation</span>
  <span class="event-meta"><svg width="13" height="13" viewBox="0 0 14 14"><circle cx="7" cy="7" r="6" stroke="#222" stroke-width="1.6" fill="none"/><path d="M7 3.5V7h2.5" stroke="#222" stroke-width="1.6" fill="none"/></svg>1 Day|Price varies</span>
  <div class="event-photo" style="background:linear-gradient(90deg,#6d4e35,#e9ecef 40%,#c9d0d6)" role="img" aria-label="Photo of white sign posts stacked in a garage"></div>
</article>
<article class="event-card" style="top:1599px">
  <span class="event-label">EVENTS</span>
  <span class="event-name">Sign Removal</span>
  <span class="event-meta"><svg width="13" height="13" viewBox="0 0 14 14"><circle cx="7" cy="7" r="6" stroke="#222" stroke-width="1.6" fill="none"/><path d="M7 3.5V7h2.5" stroke="#222" stroke-width="1.6" fill="none"/></svg>1 Day|Price varies</span>
  <div class="event-photo" style="background:linear-gradient(180deg,#8fb2d2,#7c6b55 60%,#3d3a38)" role="img" aria-label="Photo of the installer beside a truck loading a sign post"></div>
</article>

<h2 class="abs display section-title" style="left:0;width:1200px;text-align:center;top:1944px">TESTIMONIALS</h2>
<div class="avatar" style="left:122px;top:2025px" role="img" aria-label="Customer portrait"></div>
<p class="quote" style="left:200px;top:2026px">“Sed ut perspiciatis unde omnis iste nat sit voluptatem accusantium doloremque laudtium, m rem aperiam, eaque ipsa quae ab illo inventore veritatis et quasi architecto beatae vitae dicta sunt explicabo”</p>
<span class="quote-name" style="left:200px;top:2153px">Nolan E.</span>
<span class="quote-role" style="left:200px;top:2181px">Lorem ipsum dolor</span>
<div class="avatar" style="left:619px;top:2025px" role="img" aria-label="Customer portrait"></div>
<p class="quote" style="left:698px;top:2026px">“Sed ut perspiciatis unde omnis iste nat sit voluptatem accusantium doloremque laudtium, m rem aperiam, eaque ipsa quae ab illo inventore veritatis et quasi architecto beatae vitae dicta sunt explicabo”</p>
<span class="quote-name" style="left:698px;top:2153px">Priya M.</span>
<span class="quote-role" style="left:698px;top:2181px">Lorem ipsum dolor</span>

<div class="map" role="img" aria-label="Street map showing the business location"></div>

<h2 class="abs display contact-title">CONTACTUS</h2>
<p class="abs contact-lede">Lorem ipsum dolor sit amet, consectetur adipiscing elit, sed do eiusmod tempor incididunt ut</p>
<svg class="abs" style="left:136px;top:2838px" width="28" height="38" viewBox="0 0 28 38"><path d="M14 1C7 1 1 6.6 1 13.6 1 23 14 37 14 37s13-14 13-23.4C27 6.6 21 1 14 1z" fill="var(--button)"/><circle cx="14" cy="13.5" r="5" fill="#fff"/></svg>
<span class="info-label" style="top:2835px">Location:</span>
<span class="info-text" style="top:2862px">123 Avenue name, City name 10150,<br>United States</span>
<svg class="abs" style="left:136px;top:2926px" width="34" height="24" viewBox="0 0 34 24"><rect x="1" y="1" width="32" height="22" fill="none" stroke="var(--button)" stroke-width="2.5"/><path d="M1 1l16 13L33 1M1 23l12-11M33 23L21 12" stroke="var(--button)" stroke-width="2.5" fill="none"/></svg>
<span class="info-label" style="top:2922px">Email:</span>
<span class="info-text" style="top:2950px">orders@quorvaposts.example</span>
<svg class="abs" style="left:136px;top:2995px" width="30" height="30" viewBox="0 0 24 24"><path d="M6.6 10.8a15.1 15.1 0 0 0 6.6 6.6l2.2-2.2c.3-.3.7-.4 1-.2 1.1.4 2.3.6 3.6.6.6 0 1 .4 1 1V20c0 .6-.4 1-1 1C10.6 21 3 13.4 3 4c0-.6.4-1 1-1h3.5c.6 0 1 .4 1 1 0 1.3.2 2.5.6 3.6.1.3 0 .7-.2 1z" fill="var(--button)"/></svg>
<span class="info-label" style="top:2993px">Call:</span>
<span class="info-text" style="top:3021px">+1 555-014-2290</span>
<div class="field" style="left:495px;top:2837px;width:306px;height:50px">Your Name</div>
<div class="field" style="left:809px;top:2837px;width:305px;height:50px">Phone</div>
<div class="field" style="left:495px;top:2896px;width:617px;height:50px">Email</div>
<div class="field" style="left:495px;top:2953px;width:617px;height:106px">Message</div>
<a class="pill" style="left:719px;top:3075px;width:168px;height:50px">SEND MESSAGE</a>

<footer class="site-footer">
  <div class="brand" style="left:0;width:1200px;justify-content:center;top:96px;font-size:30px"><span class="brand-square"></span>Quorva Posts</div>
</footer>
<nav class="footer-nav">
  <a style="left:272px">HOME</a>
  <a style="left:394px">ABOUT US</a>
  <a style="left:528px">SERVICES</a>
  <a style="left:648px">EVENT</a>
  <a style="left:762px">REVIEW</a>
  <a style="left:901px">CONTACT US</a>
</nav>
<span class="social" style="left:515px;top:3492px"></span>
<span class="social" style="left:558px;top:3492px"></span>
<span class="social" style="left:603px;top:3492px"></span>
<span class="social" style="left:647px;top:3492px"></span>
<p class="abs copyright">© 2021 quorvaposts. All Rights Reserved.</p>

</body>
</html>
```